Real Estate Open House & For Sale Signage

I am designing brand new signs for my real estate company. All I have so far are my logo and a business card design. I would like to have designed two different signs, 1. Open House directional sign, 2. For Sale Company sign. Both signs need to will be eye catching from the street, easy to read, identifiable and memorable.

Target Market(s)

Males & females, Ages between 30-65, affluent, educated, professionals.

Industry/Entity Type

Real Estate

Font styles to use
Serif
Sans Serif

Colors
33b8a4
34a7d8
acd137
3277b5

Requirements
Must have
• Must have my company logo & real estate license number visible on the sign. Must be easily visible and eye catching from a moving vehicle. Must have a professional and trustworthy appeal. Must bring to mind real estate.
Nice to have
• Image or icon that will denote real estate and be known as a part of my company identity and marketing theme.
Should not have
• Attached is a feeble attempt at creating my For Sale sign. The information on the sign is accurate, but the design is not appealing to me at all. It feels very amateurish.

```html
<!DOCTYPE html>
<html lang="en">
<head>
<meta charset="utf-8">
<title>For Sale Sign – Makana Home Partners</title>
<link rel="stylesheet" href="https://fonts.googleapis.com/css2?family=Jost:wght@500&family=Tinos:ital,wght@0,400;0,700;1,700&display=swap">
<style>
  :root {
    --brand-green: #acd137;
    --paper: #ffffff;
    --ink: #1c1c1c;
  }
  * { margin: 0; padding: 0; box-sizing: border-box; }
  html, body {
    width: 1200px;
    height: 600px;
    overflow: hidden;
    background: var(--paper);
  }
  .sign {
    position: relative;
    width: 1200px;
    height: 600px;
    background: var(--paper);
  }
  .sale-panel {
    position: absolute;
    left: 0;
    top: 16px;
    width: 718px;
    height: 568px;
    background: var(--brand-green);
    color: var(--paper);
    text-align: center;
  }
  .headline {
    position: absolute;
    left: 0;
    right: 0;
    top: 48px;
    font-family: "Jost", sans-serif;
    font-weight: 500;
    font-size: 170px;
    line-height: 126px;
    letter-spacing: 2px;
  }
  .headline span { display: block; }
  .divider {
    position: absolute;
    left: 332px;
    top: 350px;
    width: 68px;
    height: 6px;
    background: var(--paper);
  }
  .agent-name {
    position: absolute;
    left: 0;
    right: 0;
    top: 384px;
    font-family: "Tinos", serif;
    font-style: italic;
    font-weight: 700;
    font-size: 52px;
    line-height: 1;
  }
  .agent-phone {
    position: absolute;
    left: 0;
    right: 0;
    top: 442px;
    font-family: "Tinos", serif;
    font-weight: 700;
    font-size: 41px;
    line-height: 1;
  }
  .agent-license {
    position: absolute;
    left: 0;
    right: 0;
    top: 512px;
    font-family: "Tinos", serif;
    font-size: 18px;
    letter-spacing: 2px;
    line-height: 1;
  }
  .brand {
    position: absolute;
    left: 735px;
    width: 450px;
    top: 260px;
    text-align: center;
  }
  .brand-name {
    font-family: "Jost", sans-serif;
    font-weight: 500;
    font-size: 40px;
    line-height: 1.15;
    letter-spacing: 6px;
    color: var(--brand-green);
  }
  .brand-license {
    margin-top: 58px;
    font-family: "Tinos", serif;
    font-size: 21px;
    letter-spacing: 2px;
    color: var(--ink);
  }
</style>
</head>
<body>
  <main class="sign">
    <section class="sale-panel">
      <h1 class="headline"><span>FOR</span><span>SALE</span></h1>
      <div class="divider"></div>
      <p class="agent-name">Leilani Ross</p>
      <p class="agent-phone">(808) 555-0142</p>
      <p class="agent-license">RB-10452</p>
    </section>
    <section class="brand">
      <p class="brand-name">MAKANA HOME<br>PARTNERS LLC</p>
      <p class="brand-license">RB-30871</p>
    </section>
  </main>
</body>
</html>
```